Page Layouts for Australian Political Party

The Forward Signal Party of Australia has a design for its logo and now is looking for a website proposal. The initial website is being powered by blogger with plans to move to an ExpressionEngine based site. The current website is at www.fspartyhub.org

Its likely if we see a design within the next 2 days we like it will be selected before the 5 days has expired.

Target Market(s)

Looking for a design that will appeal to both the "online" generation as well as more casual internet users. These users might be comfortable with online banking and perhaps mailnest/talkloop but not much more.

I personally like the "feel" of vimrol.com and plumtreelabs.com. You might like to look at the other major political parties in Australia to see what probably quite a lot of "market testing" and money is acceptable to the Australian population. We are aiming for Generation X and younger and well as the baby boomers who get the 2.0 internet.

Industry/Entity Type

Political

Requirements
Must have
• The ability to scale elegantly across a full ExpressionEngine implementation, forums, blogs, homepage etc.
• Also look elegant on the initial blogger driven page.
• Navigation that could contain all the items on the www.unityfront.org.au site, you can use these as the place holder names for the navigation design. The short name for the party is FSP. The
Nice to have
• feel distinct from the other major parties websites. we do have views more in line with the orchardists/reformists in this country.
Should not have
• basic stuff, not look like a pagenook page ;) imagery too similar from any of the other parties...

```html
<!DOCTYPE html>
<html lang="en">
<head>
<meta charset="utf-8">
<title>Forward Signal Party of Australia</title>
<link rel="stylesheet" href="https://fonts.googleapis.com/css2?family=Arimo:wght@400;700&family=Archivo+Black&display=swap">
<style>
:root{
  --page-bg:#e4e3e4;
  --column:#efeeef;
  --ink:#111;
  --link-blue:#1b6e9c;
  --band-dark:#5a5a5a;
  --caption:#6c6c6c;
  --panel:#ffffff;
  --title-grey:#6a6a6a;
}
*{margin:0;padding:0;box-sizing:border-box}
html,body{width:800px;height:1200px;overflow:hidden;background:var(--page-bg);font-family:"Arimo",Arial,sans-serif}
.page{position:relative;width:800px;height:1200px;background:linear-gradient(90deg,#d8d7d8 0,#e6e5e6 80px,#e6e5e6 720px,#d8d7d8 800px)}
.column{position:absolute;left:80px;top:0;width:642px;height:1200px;background:var(--column);box-shadow:0 0 6px rgba(0,0,0,.25)}
.header-top{position:absolute;left:80px;top:11px;width:640px;height:42px;background:linear-gradient(#fff,#f0f0f0)}
.header-band{position:absolute;left:80px;top:53px;width:640px;height:98px;background:linear-gradient(#8d8d8d,#c9c9c9 45%,#ececec);box-shadow:0 4px 8px rgba(0,0,0,.3)}
.utility{position:absolute;right:112px;top:32px;font-size:12px;color:var(--link-blue)}
.utility span{margin:0 8px}
.utility b{font-weight:700}
.brand{position:absolute;left:104px;top:96px;display:flex;align-items:center;gap:8px;font-size:24px;color:#222;letter-spacing:-.5px}
.brand i{display:block;width:18px;height:18px;background:var(--link-blue)}
.nav{position:absolute;left:103px;top:131px;font-size:12px;letter-spacing:.4px;color:var(--ink);white-space:nowrap}
.nav b{font-weight:700}
.tab{position:absolute;height:24px;background:linear-gradient(#fff,#e2e2e2);border-radius:3px 3px 0 0;box-shadow:0 1px 3px rgba(0,0,0,.3);font-size:12px;letter-spacing:1px;color:#aaa;padding:6px 9px;white-space:nowrap}
.tab b{color:#888;font-weight:700}
.hero{position:absolute;left:114px;top:190px;width:576px;height:309px;border-radius:8px;overflow:hidden;box-shadow:0 2px 6px rgba(0,0,0,.4)}
.hero-photo{height:246px;background:radial-gradient(ellipse at 60% 45%,#c98f6c,#9a5a36 45%,#5e3218 80%)}
.hero-caption{height:63px;background:var(--caption);color:#fff;padding:6px 18px}
.hero-caption h2{font-size:13px;font-weight:400;letter-spacing:1px}
.hero-caption h3{font-size:8px;font-weight:700;margin-top:2px}
.hero-caption p{font-size:7px;line-height:11px;margin-top:2px;color:#eee}
.idea-tab{position:absolute;left:114px;top:561px;width:32px;height:117px;background:linear-gradient(90deg,#fff,#dcdcdc);border-radius:4px 0 0 4px;box-shadow:0 1px 3px rgba(0,0,0,.3)}
.idea-tab span{position:absolute;left:6px;top:104px;transform:rotate(-90deg);transform-origin:0 0;font-size:12px;letter-spacing:1px;color:#aaa;white-space:nowrap}
.idea-tab b{color:#888}
.idea-panel{position:absolute;left:142px;top:516px;width:550px;height:197px;background:linear-gradient(#f6f6f6,#e8e8e8);border-radius:40px;box-shadow:0 2px 6px rgba(0,0,0,.35);overflow:hidden}
.idea-cta{position:absolute;left:0;top:0;width:160px;height:197px;background:var(--panel);box-shadow:2px 0 5px rgba(0,0,0,.2);font-family:"Archivo Black",Arial,sans-serif;color:#333;text-shadow:2px 2px 3px rgba(0,0,0,.35);padding:20px 0 0 16px;line-height:.95;white-space:nowrap}
.idea-cta .l1{font-size:44px;letter-spacing:-1px}
.idea-cta .l2{font-size:24px;letter-spacing:-1px}
.idea-cta .l3{font-size:34px;letter-spacing:-1.5px}
.idea-cta .l4{font-size:40px;letter-spacing:-1.5px}
.idea-post{position:absolute;top:14px;width:168px;height:175px}
.idea-post h4{font-size:16px;line-height:19px;color:var(--title-grey);font-weight:700}
.idea-post p{font-size:11px;line-height:19px;color:#666;margin-top:4px}
.read-more{position:absolute;right:0;font-size:9px;font-weight:700;color:#111;text-decoration:underline}
.divider{position:absolute;left:346px;top:18px;width:1px;height:160px;background:#ccc}
.news-band{position:absolute;left:80px;top:736px;width:642px;height:299px;background:linear-gradient(#e9e9e9 0,#9a9a9a 140px,#5c5c5c 200px,var(--band-dark))}
.card{position:absolute;top:781px;width:176px;height:118px;background:linear-gradient(#fff,#d5d5d5);border-radius:3px;box-shadow:0 1px 3px rgba(0,0,0,.3)}
.card .photo{position:absolute;top:4px;height:110px;box-shadow:1px 1px 3px rgba(0,0,0,.4)}
.story{position:absolute;top:912px;width:176px;color:#fff}
.story h5{font-size:18px;font-weight:700;color:#3c3c3c;text-shadow:1px 1px 0 #ccc;letter-spacing:-.3px;white-space:nowrap}
.story p{font-size:9.6px;line-height:11.2px;margin-top:6px;text-align:justify}
.story .more{position:absolute;right:0;top:97px;font-size:8.5px;color:#eee;letter-spacing:.5px}
.footer{position:absolute;left:80px;top:1035px;width:640px;text-align:center;font-size:9.8px;color:#444}
.footer p{position:absolute;width:100%}
.footer-bottom{position:absolute;left:80px;top:1158px;width:640px;height:42px;background:linear-gradient(#e2e2e2,#a6a6a6);text-align:center;font-size:9.8px;color:#e9e9e9;padding-top:20px}
</style>
</head>
<body>
<div class="page">
  <div class="column"></div>

  <header>
    <div class="header-top"></div>
    <div class="header-band"></div>
    <div class="utility">Contact Us<span>|</span>The Blog<span>|</span><b>LOGIN</b></div>
    <div class="brand"><i></i>Forward Signal</div>
    <nav class="nav"><b>Home</b> . About Us . Structure . Services . Links . Resources . News &amp; Events . Community . Get Involved</nav>
  </header>

  <div class="tab" style="left:132px;top:166px;width:96px">UNITY . <b>TV</b></div>
  <section class="hero">
    <div class="hero-photo" role="img" aria-label="Video still of a party leader speaking at a debate"></div>
    <div class="hero-caption">
      <h2>Daniel Ashcroft</h2>
      <h3>Civic Speakers Forum Health Debate Opening and Closing Statements.</h3>
      <p>Before the election, Mr Hallett said that he would fix public hospitals by the middle of last year. It's probably his biggest single broken promise...</p>
    </div>
  </section>

  <div class="idea-tab"><span>YOUR . <b>IDEA</b></span></div>
  <section class="idea-panel">
    <div class="idea-cta"><div class="l1">ADD</div><div class="l2">AN IDEA</div><div class="l3">START</div><div class="l4">NOW!</div></div>
    <article class="idea-post" style="left:175px">
      <h4>Monarchy/Replublic? - Education Needed.</h4>
      <p>No doubt the Republic issue will raise its head in the not too distant future.I propose that if any decision is to be made, that...</p>
      <span class="read-more" style="top:152px">Read More..</span>
    </article>
    <div class="divider"></div>
    <article class="idea-post" style="left:357px">
      <h4>Revocation of Citizenship &amp; Tighter Rulings on gaining Citizenship.</h4>
      <p>1) Citizenship of Australia should be a privilege not an automatic right. If you are a new citizen or are the childr&nbsp; en of new...</p>
      <span class="read-more" style="top:152px">Read More..</span>
    </article>
  </section>

  <div class="news-band"></div>
  <div class="tab" style="left:131px;top:737px;width:124px">LATEST . <b>NEWS</b></div>

  <div class="card" style="left:117px"><div class="photo" role="img" aria-label="Photo of a politician at a media doorstop" style="left:29px;width:118px;background:linear-gradient(#7fa9c4,#6d6560)"></div></div>
  <div class="card" style="left:312px"><div class="photo" role="img" aria-label="Portrait photo of a shadow minister" style="left:32px;width:112px;background:linear-gradient(#6b5a3c,#4a4040)"></div></div>
  <div class="card" style="left:513px"><div class="photo" role="img" aria-label="Portrait photo of a party spokesperson" style="left:34px;width:110px;background:linear-gradient(#9a8a5c,#a9b8c6)"></div></div>

  <article class="story" style="left:117px">
    <h5>Ashcroft Doorstop</h5>
    <p>Opening of Unity House Westmere, border protection and Shadow Ministerial arrangements. Mr Hallett has lost control of our borders and because he has lost control he's lost interest...</p>
    <span class="more">Read More..</span>
  </article>
  <article class="story" style="left:312px">
    <h5>Shadow Ministerial</h5>
    <p>Changes to Shadow Ministerial arrangements. Following the announcement yesterday by Senator the Hon. Neil Marston that he will not stand at the next election, the following...</p>
    <span class="more">Read More..</span>
  </article>
  <article class="story" style="left:513px">
    <h5>Meridian Boat 97</h5>
    <p>No more excuses for Meridian as boat 97 arrives. Brings the total number of illegal boat arrivals for 2010 to 29 boats and almost 1500 people...</p>
    <span class="more">Read More..</span>
  </article>

  <footer>
    <div class="footer">
      <p style="top:30px">Corvane combines the most powerful features of collaboration software, community software,</p>
      <p style="top:46px">social networking software &amp; social media monitoring into the leading SBS solution.</p>
      <p style="top:78px">© Copyright 2000–2010 Corvane Works. All rights reserved.</p>
      <p style="top:110px">Sales: 800-555-0142 | General: 800-555-0187</p>
    </div>
    <div class="footer-bottom">Privacy Policy | Sitemap | Jobs | Contact Us</div>
  </footer>
</div>
</body>
</html>
```